Marketing company needs business card design

Our company (Bright Harbor Partners) need a business card design for a marketing company. The design should of course include the logo and business colors (orange and blue). I would like the design to be clean and professional. The business card is going to be a die cut card that is leaf shaped (I have uploaded the template for it). I would love to see a design that is professional but nothing too "corporate."
Updates

Hello everyone,

Just wanted to let you know that I have uploaded an AI and EPS version of the logo for your convenience.

Thank you!

~Miranda

Industry/Entity Type

Marketing

Requirements
Must have
• Must have the following contact info:

Bright Harbor Partners
2871 Cedar Hollow Rd B204
Prescott, AZ 86301

928.614.3827

info@brightharborpartners-example.com

```html
<!DOCTYPE html>
<html lang="en">
<head>
<meta charset="utf-8">
<title>Bright Harbor Partners – Business Card</title>
<link rel="stylesheet" href="https://fonts.googleapis.com/css2?family=Source+Sans+3:wght@400;600;700&display=swap">
<style>
  :root {
    --backdrop: #b0713f;
    --brand-blue: #13a9e3;
    --brand-orange: #eda95e;
    --card-white: #ffffff;
    --text-blue: #1a9fd8;
  }
  * { margin: 0; padding: 0; box-sizing: border-box; }
  html, body {
    width: 1152px;
    height: 1200px;
    overflow: hidden;
    background: var(--backdrop);
    font-family: "Source Sans 3", "Helvetica Neue", Arial, sans-serif;
  }
  .canvas {
    position: relative;
    width: 1152px;
    height: 1200px;
  }
  .card {
    position: absolute;
    left: 144px;
    width: 864px;
  }
  .card-front {
    top: 86px;
    height: 492px;
    background: var(--brand-blue);
    border-radius: 150px 0 190px 0;
    display: flex;
    align-items: center;
    justify-content: center;
  }
  .card-back {
    top: 624px;
    height: 514px;
    background: var(--card-white);
    border-radius: 0 190px 0 150px;
  }
  .brand {
    display: flex;
    align-items: center;
    gap: 28px;
    font-weight: 600;
    line-height: 1.02;
  }
  .brand-dot {
    flex: none;
    border-radius: 50%;
    background: var(--brand-orange);
  }
  .card-front .brand {
    color: var(--card-white);
    font-size: 88px;
  }
  .card-front .brand-dot { width: 110px; height: 110px; }
  .card-back .brand {
    position: absolute;
    right: 84px;
    top: 74px;
    color: var(--text-blue);
    font-size: 68px;
  }
  .card-back .brand-dot { width: 84px; height: 84px; }
  .contact {
    position: absolute;
    right: 60px;
    top: 276px;
    width: 560px;
    text-align: right;
    color: var(--text-blue);
    font-size: 23px;
    line-height: 34px;
    white-space: nowrap;
  }
  .contact-name { font-weight: 700; }
  .contact-rule {
    width: 420px;
    height: 2px;
    margin: 10px 0 10px auto;
    background: linear-gradient(to right, rgba(237,169,94,0), var(--brand-orange) 35%);
  }
  .contact-line {
    display: flex;
    justify-content: flex-end;
    align-items: center;
    gap: 12px;
  }
  .contact-line svg { flex: none; }
  .icon-slot { width: 20px; display: flex; justify-content: center; }
</style>
</head>
<body>
<main class="canvas">
  <section class="card card-front">
    <div class="brand">
      <span class="brand-dot"></span>
      <span class="brand-name">Bright Harbor<br>Partners</span>
    </div>
  </section>

  <section class="card card-back">
    <div class="brand">
      <span class="brand-dot"></span>
      <span class="brand-name">Bright Harbor<br>Partners</span>
    </div>

    <div class="contact">
      <p class="contact-name">Bright Harbor Partners</p>
      <p class="contact-address">2871 Cedar Hollow Rd B204<br>Prescott, AZ 86301</p>
      <div class="contact-rule"></div>
      <p class="contact-line">928.614.3827
        <span class="icon-slot">
          <svg width="14" height="20" viewBox="0 0 14 20" aria-hidden="true">
            <rect x="1.5" y="1" width="11" height="18" rx="2" fill="none" stroke="var(--brand-orange)" stroke-width="2"/>
            <rect x="4" y="4" width="6" height="5" fill="var(--brand-orange)"/>
            <circle cx="7" cy="14.5" r="1.5" fill="var(--brand-orange)"/>
          </svg>
        </span>
      </p>
      <p class="contact-line">info@brightharborpartners-example.com
        <span class="icon-slot">
          <svg width="20" height="14" viewBox="0 0 20 14" aria-hidden="true">
            <rect x="0" y="0" width="20" height="14" rx="1.5" fill="var(--brand-orange)"/>
            <path d="M1 1 L10 8 L19 1" fill="none" stroke="var(--card-white)" stroke-width="1.6"/>
          </svg>
        </span>
      </p>
    </div>
  </section>
</main>
</body>
</html>
```